Managed Service provider for IT support needs a three panel fold flyer

We are a Information & Technology company, providing compelte managed services ot the SMB market in southern Califonia.
Looking for a three panel, tri-fold or other, 3.75 X 8.35 Vertical flyer.
The final design should communicate a partnered techjnology solution

Managed Services:
Designed to reduce your costs, increase your profits and mitigate your business risks, we partner with you as your Virtual IT Department, allowing you to focus on running your business, not your technology.

https://brixolane.com/

It Company

```html
<!DOCTYPE html>
<html lang="en">
<head>
<meta charset="utf-8">
<title>Brixolane Computer Service – Tri-fold Flyer</title>
<link href="https://fonts.googleapis.com/css2?family=Open+Sans:wght@400;600;700&family=Oswald:wght@200;300&display=swap" rel="stylesheet">
<style>
  :root{
    --backdrop:#5f5f5f;
    --brand-blue:#1272bd;
    --brand-navy:#0d4f86;
    --ink:#1a1a1a;
    --paper:#ffffff;
    --numeral:#a9a9ad;
    --pill:#0b0b0b;
  }
  *{box-sizing:border-box;margin:0;padding:0}
  html,body{width:1200px;height:1200px;overflow:hidden;background:var(--backdrop)}
  body{font-family:"Open Sans",Arial,sans-serif;color:var(--ink);position:relative}

  .spread{position:absolute;left:197px;width:806px;height:570px;background:var(--paper);overflow:hidden}
  .spread--outside{top:26px}
  .spread--inside{top:605px}

  /* ---------- Outside: benefits panel ---------- */
  .benefits{position:absolute;left:0;top:0;width:269px;height:570px;background:var(--paper)}
  .benefit{position:absolute;left:0;width:269px}
  .benefit h3{position:absolute;left:22px;top:0;font-size:15px;font-weight:600;color:var(--brand-blue);white-space:nowrap}
  .benefit .numeral{position:absolute;left:24px;top:22px;font-family:"Oswald",sans-serif;font-weight:200;font-size:72px;line-height:1;color:var(--numeral)}
  .benefit p{position:absolute;left:57px;top:27px;width:200px;font-size:9.4px;line-height:11.6px}

  /* ---------- Outside: contact panel ---------- */
  .cta{position:absolute;left:269px;top:0;width:269px;height:101px;background:var(--brand-blue);color:#fff;
       display:flex;align-items:center;justify-content:center;text-align:center;font-weight:700;font-size:14.5px;line-height:18px}
  .team-photo{position:absolute;left:269px;top:101px;width:537px;height:230px;
       background:linear-gradient(100deg,#9aa3ab 0%,#e8ebee 30%,#c9ced3 55%,#f3f3f3 80%,#d8d8d8 100%)}
  .contact{position:absolute;left:269px;top:331px;width:269px;height:239px;background:var(--brand-blue);color:#fff;text-align:center}
  .contact-tab{position:absolute;left:58px;top:-17px;width:154px;height:32px;background:var(--brand-navy);
       font-weight:700;font-size:19px;line-height:32px;color:#fff}
  .contact .phone{position:absolute;left:0;right:0;top:25px;font-size:18.5px;display:flex;justify-content:center;align-items:center;gap:6px}
  .contact .email{position:absolute;left:0;right:0;top:53px;font-size:12.5px;display:flex;justify-content:center;align-items:center;gap:7px}
  .contact .wordmark{position:absolute;left:0;right:0;top:88px;font-weight:700;font-size:30px;letter-spacing:.5px}
  .contact .wordmark small{display:block;font-size:8px;font-weight:400;letter-spacing:4px;margin-top:-4px}
  .social{position:absolute;left:0;right:0;top:148px;display:flex;justify-content:center;gap:4px}
  .social span{width:32px;height:32px;border-radius:50%;background:var(--brand-navy)}
  .contact .url{position:absolute;left:0;right:0;top:197px;font-weight:700;font-size:16.5px}

  /* ---------- Outside: cover panel ---------- */
  .cover{position:absolute;left:538px;top:0;width:268px;height:570px}
  .cover .wordmark{position:absolute;left:22px;top:20px;font-weight:700;font-size:46px;line-height:46px;color:var(--brand-blue)}
  .cover .wordmark small{display:block;font-size:10px;line-height:12px;font-weight:400;letter-spacing:4.4px;color:var(--ink);text-align:right}
  .cover .tagline{position:absolute;left:32px;top:79px;font-size:10.5px;font-style:italic}
  .cover h1{position:absolute;left:32px;top:349px;font-size:32px;line-height:37px;font-weight:700;color:var(--ink)}
  .cover .lede{position:absolute;left:32px;top:502px;width:220px;font-size:12px;line-height:14px}

  /* ---------- Inside: expertise panel ---------- */
  .expertise{position:absolute;left:0;top:0;width:269px;height:570px;
       background:linear-gradient(160deg,#f7f7f7 0%,#e6e7e9 60%,#f1f1f1 100%)}
  .expertise h2{position:absolute;left:0;right:0;top:32px;text-align:center;font-size:20px;font-weight:700;color:var(--brand-blue)}
  .strip{position:absolute;left:0;width:269px}
  .strip--cloud{top:100px;height:113px;background:linear-gradient(90deg,#5d6570,#aab3bd 60%,#d9dde1)}
  .strip--comms{top:213px;height:118px;background:linear-gradient(135deg,#0e3f78,#2c7fc4 55%,#7fc0ee)}
  .strip--security{top:331px;height:112px;background:linear-gradient(90deg,#3d86c6,#a6d3f2 55%,#5e9fd4)}
  .strip--mobility{top:443px;height:127px;background:linear-gradient(120deg,#1a2330,#3b5f86 60%,#8fb4d8)}
  .strip-label{position:absolute;left:0;top:0;height:28px;padding:0 30px 0 22px;border-radius:0 0 28px 0;
       background:var(--brand-blue);color:#fff;font-size:12px;line-height:28px;white-space:nowrap}

  /* ---------- Inside: services panel ---------- */
  .services{position:absolute;left:269px;top:0;width:537px;height:570px;
       background:linear-gradient(180deg,#2b3e55 0%,#6d7f93 12%,#dfe3e8 20%,#f6f7f8 30%,#ffffff 100%)}
  .services h2{position:absolute;left:0;right:0;top:34px;text-align:center;color:#fff;font-size:19.5px;font-weight:700}
  .services .pill{position:absolute;left:56px;top:62px;width:429px;height:28px;border-radius:14px;background:var(--pill);
       color:#fff;font-size:9.6px;line-height:28px;text-align:center}
  .service{position:absolute;width:240px}
  .service h3{font-size:15px;font-weight:600;color:var(--brand-blue);white-space:nowrap}
  .service p{margin:18px 0 0 35px;width:190px;font-size:9.4px;line-height:11.6px}
  .col-a{left:22px}.col-b{left:289px}
  .row-1{top:105px}.row-2{top:264px}.row-3{top:411px}
</style>
</head>
<body>

<section class="spread spread--outside">
  <div class="benefits">
    <div class="benefit" style="top:34px">
      <h3>Security Solutions</h3><span class="numeral">1</span>
      <p>Intrusion, hacking and electronic theft attempts against businesses of all types and sizes are increasing exponentially, and our network security services in Larkfield, CA cost-effectively protect and maintain the security of your network, assets and data against attack, providing you peace of mind.</p>
    </div>
    <div class="benefit" style="top:174px">
      <h3>Cloud Solutions</h3><span class="numeral">2</span>
      <p>Does your business demand greater performance, rapid scalability and higher availability from your line of business and productivity applications to remain competitive? Stop paying the high cost of traditional software in Larkfield, CA – simply pay one low, flat fee per month!</p>
    </div>
    <div class="benefit" style="top:306px">
      <h3>Managed IT</h3><span class="numeral">3</span>
      <p>We deliver proactive flat-rate IT Managed Services in Larkfield, CA. Designed to reduce your costs, increase your profits and mitigate your business risks, we partner with you as your Virtual IT Department, allowing you to focus on running your business, not your technology.</p>
    </div>
    <div class="benefit" style="top:430px">
      <h3>Mobility Solutions</h3><span class="numeral">4</span>
      <p>Smartphones and Tablets are fueling mobile computing. The ability to remain connected is now a reality – whether at home, vacation or business traveling. Increase business productivity by enabling secure mobile computing accessibility for your business in Larkfield, CA.</p>
    </div>
  </div>

  <div class="cta">Find out how our IT Solutions<br>can help your organization!</div>
  <div class="team-photo" role="img" aria-label="Photo of a smiling support team with headsets at computer monitors in an office"></div>

  <div class="contact">
    <div class="contact-tab">Contact Us</div>
    <div class="phone">
      <svg width="14" height="16" viewBox="0 0 24 24" aria-hidden="true"><path fill="#fff" d="M6.6 10.8a15.1 15.1 0 0 0 6.6 6.6l2.2-2.2a1 1 0 0 1 1-.25 11.4 11.4 0 0 0 3.6.57 1 1 0 0 1 1 1V20a1 1 0 0 1-1 1A17 17 0 0 1 3 4a1 1 0 0 1 1-1h3.5a1 1 0 0 1 1 1c0 1.25.2 2.45.57 3.57a1 1 0 0 1-.25 1z"/></svg>
      (555) 014-2280
    </div>
    <div class="email">
      <svg width="16" height="11" viewBox="0 0 16 11" aria-hidden="true"><rect x=".5" y=".5" width="15" height="10" fill="none" stroke="#fff"/><path d="M.5.5 8 6.5 15.5.5" fill="none" stroke="#fff"/></svg>
      support@brixolane.com
    </div>
    <div class="wordmark">Brixolane<small>computer service</small></div>
    <div class="social"><span></span><span></span></div>
    <div class="url"><a href="https://brixolane.com/" style="color:inherit;text-decoration:none">brixolane.com</a></div>
  </div>

  <div class="cover">
    <div class="wordmark">Brixolane<small>computer service</small></div>
    <p class="tagline">“Timely IT support to power your Business”</p>
    <h1>Technology<br>Management<br>Consulting<br>Services</h1>
    <p class="lede">Delivering quality IT solutions, support and services tailored to your specific business needs</p>
  </div>
</section>

<section class="spread spread--inside">
  <div class="expertise">
    <h2>Our Expertise</h2>
    <div class="strip strip--cloud" role="img" aria-label="Photo of a businesswoman with a smartphone beside server racks and floating file icons"><span class="strip-label">Cloud Solutions</span></div>
    <div class="strip strip--comms" role="img" aria-label="Illustration of a hand touching a network of connected user icons"><span class="strip-label">Unified Communications</span></div>
    <div class="strip strip--security" role="img" aria-label="Illustration of a padlock surrounded by device and communication icons"><span class="strip-label">Security</span></div>
    <div class="strip strip--mobility" role="img" aria-label="Photo of a hand holding a smartphone"><span class="strip-label">Mobility</span></div>
  </div>

  <div class="services">
    <h2>Some of our Services</h2>
    <div class="pill">We tailor our cost-effective IT services and solutions to meet your specific business needs</div>

    <div class="service col-a row-1"><h3>Managed IT Services</h3>
      <p>We deliver proactive flat-rate Managed IT Services in Larkfield, CA. Designed to reduce your costs, eliminate business pain, increase your profits and mitigate business risks, we partner with you as your Virtual IT Department and outsourced CTO, allowing you to focus on running your business, not your technology.</p></div>
    <div class="service col-b row-1"><h3>Manufacturing IT Services</h3>
      <p>Do you need an IT firm experienced in supporting your manufacturing processes, equipment and specialized line of business applications? Our manufacturing IT services in Larkfield, CA include remote and onsite system and software support, 24×7 network monitoring, patching and updating and more.</p></div>
    <div class="service col-a row-2"><h3>Healthcare IT Services</h3>
      <p>Do you need a HIPAA and HiTech-compliant Healthcare IT Service Provider? Does your practice require expert EMR and Practice Management Software support? Would you like to reduce the cost and complexity of your technology? Our Healthcare Technology Solutions in Larkfield, CA are the answer.</p></div>
    <div class="service col-b row-2"><h3>Accounting IT Services</h3>
      <p>Are you seeking an IT firm experienced in supporting the multiple versions of your Accounting Practice’s specific line of business software applications? Would you like to increase the security and availability of your network? Our Accounting Technology Solutions in Larkfield, CA are the answer.</p></div>
    <div class="service col-a row-3"><h3>Engineering IT Services</h3>
      <p>Are you seeking an IT firm experienced in supporting your Engineering processes, equipment and software applications? Would you like to reduce the cost and complexity of your technology and increase uptime? We deliver complete Engineering Technology Solutions in Larkfield, CA.</p></div>
    <div class="service col-b row-3"><h3>Legal IT Services</h3>
      <p>Do you need an IT firm versed in supporting your legal processes and applications, e-discovery, archiving and secure document management? Increase the security and availability of your critical data, systems and services with our Legal Technology Solutions in Larkfield, CA.</p></div>
  </div>
</section>

</body>
</html>
```